Business Card Design

Supporting people with a spinal cord injury

Industry/Entity Type

Business

Contact Information for Business Card

FRONT
Marcy Quellton
Service Coordinator
57 Fenwick Lane, West Mackay QLD 4740
Tel: (07) 4063 8815
Fax: (07) 4063 8819
after hours: 0498761137
marcy@trovex.org.au
www.trovex.org.au

BACK - little text to fit
* Personal care and lifestyle assistance
* Supported accommodation - temporary, respite and transition (Kolo-haven)
* Transition Support Program for residents of Kolo-haven with a SCI
* In-home respite support
* Community Access
* In-home support for people in the community
* Wheelchair accessible transport
* Equipment loan
* Use of Brisk core Gym to work on upper body strength
* SCI awareness and prevention
* Information and community linking
* Assist people with obtaining equipment
* 3 accessible, 2bedroom rental units in Andergrove
* After hours emergency support service
BEINF INSPIRED AND INSPIRING OTHERS

```html
<!DOCTYPE html>
<html lang="en">
<head>
<meta charset="utf-8">
<title>Trovex business cards</title>
<link rel="stylesheet" href="https://fonts.googleapis.com/css2?family=Orbitron:wght@700&family=Roboto+Condensed:wght@400&display=swap">
<style>
  :root {
    --stage: #8e8e8e;
    --card-dark: #231f20;
    --card-light: #ffffff;
    --ink-light: #ffffff;
    --ink-dark: #231f20;
    --accent-red: #e31e2e;
    --accent-purple: #8a77b8;
  }
  * { margin: 0; padding: 0; box-sizing: border-box; }
  html, body { width: 1200px; height: 1000px; overflow: hidden; }
  body {
    position: relative;
    background: var(--stage);
    font-family: "Roboto Condensed", Arial, sans-serif;
  }
  .card {
    position: absolute;
    width: 482px;
    height: 297px;
    box-shadow: 3px 4px 8px rgba(0,0,0,0.35);
    overflow: hidden;
  }
  .card--dark { background: var(--card-dark); color: var(--ink-light); }
  .card--light { background: var(--card-light); color: var(--ink-dark); }
  .card--front { left: 49px; top: 33px; }
  .card--back-dark { left: 607px; top: 33px; }
  .card--back-light { left: 607px; top: 357px; }

  .front-mark {
    position: absolute;
    left: 32px;
    top: 100px;
    width: 100px;
    height: 100px;
    border-radius: 50%;
    background: var(--accent-purple);
  }
  .holder-name {
    position: absolute;
    left: 235px;
    top: 27px;
    font-family: "Orbitron", Arial, sans-serif;
    font-weight: 700;
    font-size: 19px;
    color: var(--accent-red);
    letter-spacing: 0.3px;
  }
  .holder-role {
    position: absolute;
    left: 236px;
    top: 52px;
    font-size: 12px;
  }
  .contact-list {
    position: absolute;
    left: 236px;
    top: 141px;
    list-style: none;
  }
  .contact-list li {
    display: flex;
    align-items: center;
    height: 20px;
    font-size: 12.5px;
  }
  .contact-icon {
    width: 13px;
    height: 13px;
    margin-right: 5px;
    flex: none;
  }

  .brand {
    position: absolute;
    left: 40px;
    top: 0;
    height: 100%;
    display: flex;
    align-items: center;
    gap: 22px;
  }
  .brand-dot {
    width: 64px;
    height: 64px;
    border-radius: 50%;
    background: var(--accent-purple);
    flex: none;
  }
  .brand-text { display: flex; flex-direction: column; }
  .brand-name {
    font-size: 78px;
    line-height: 0.9;
    letter-spacing: 1px;
  }
  .brand-full {
    font-size: 12.5px;
    margin-top: 6px;
  }
  .card--back-light .brand-full { color: #8a8a8a; }
</style>
</head>
<body>

  <section class="card card--dark card--front" aria-label="Business card front">
    <div class="front-mark"></div>
    <p class="holder-name">Marcy Quellton</p>
    <p class="holder-role">Service Coordinator</p>
    <ul class="contact-list">
      <li>
        <svg class="contact-icon" viewBox="0 0 13 13"><rect width="13" height="13" rx="2" fill="#fff"/><rect x="4" y="2" width="5" height="9" rx="1" fill="none" stroke="#231f20" stroke-width="1.2"/></svg>
        0498761137
      </li>
      <li>
        <svg class="contact-icon" viewBox="0 0 13 13"><rect width="13" height="13" rx="2" fill="#fff"/><path d="M4 2.5c-1 1-1 3 1 5.5s4 3 5 2l-1.5-1.8-1.3.6c-.8-.4-1.6-1.3-2-2.1l.6-1.3z" fill="#231f20"/></svg>
        (07) 4063 8815
      </li>
      <li>
        <svg class="contact-icon" viewBox="0 0 13 13"><rect width="13" height="13" rx="2" fill="#fff"/><rect x="2.5" y="5" width="8" height="5.5" fill="#231f20"/><rect x="4" y="2.5" width="5" height="3" fill="#231f20"/></svg>
        (07) 4063 8819
      </li>
      <li>
        <svg class="contact-icon" viewBox="0 0 13 13"><rect width="13" height="13" rx="2" fill="#fff"/><rect x="2.5" y="3.5" width="8" height="6" fill="none" stroke="#231f20" stroke-width="1.1"/><path d="M2.5 3.5l4 3.5 4-3.5" fill="none" stroke="#231f20" stroke-width="1.1"/></svg>
        marcy@trovex.org.au
      </li>
      <li>
        <svg class="contact-icon" viewBox="0 0 13 13"><rect width="13" height="13" rx="2" fill="#fff"/><circle cx="6.5" cy="6.5" r="4" fill="none" stroke="#231f20" stroke-width="1"/><path d="M2.5 6.5h8M6.5 2.5c-2 2.5-2 5.5 0 8M6.5 2.5c2 2.5 2 5.5 0 8" fill="none" stroke="#231f20" stroke-width="0.9"/></svg>
        www.trovex.org.au
      </li>
      <li>
        <svg class="contact-icon" viewBox="0 0 13 13"><rect width="13" height="13" rx="2" fill="#fff"/><path d="M6.5 11s-3.2-3.4-3.2-5.6a3.2 3.2 0 0 1 6.4 0C9.7 7.6 6.5 11 6.5 11z" fill="#231f20"/><circle cx="6.5" cy="5.4" r="1.1" fill="#fff"/></svg>
        57 Fenwick Lane, West Mackay QLD 4740
      </li>
    </ul>
  </section>

  <section class="card card--dark card--back-dark" aria-label="Business card back, dark">
    <div class="brand">
      <div class="brand-dot"></div>
      <div class="brand-text">
        <span class="brand-name">TROVEX</span>
        <span class="brand-full">Trovex Spinal Support Association Inc</span>
      </div>
    </div>
  </section>

  <section class="card card--light card--back-light" aria-label="Business card back, light">
    <div class="brand">
      <div class="brand-dot"></div>
      <div class="brand-text">
        <span class="brand-name">TROVEX</span>
        <span class="brand-full">Trovex Spinal Support Association Inc</span>
      </div>
    </div>
  </section>

</body>
</html>
```